Fresh, modern, fun business card for pediatric dental practice

Need a business card for fresh, modern, fun pediatric dental practice

Clean look that matches our website's font and colors

We prefer the look of curved corners on business cards

Target Market(s)

parents (mothers) of young children, professionals, mid-high class

Industry/Entity Type

Dental

Contact Information for Business Card

Maplebrook Pediatric Dentistry
482 Orchard Vale Road
Suite 517
Fernhollow, PA 17000
555.419.3067
www.maplebrookkidsdental.example

Mara Tevlin, DMD
Colette Varnum, DMD
(we are working on our email address, but we would like that on the card as well)

Font styles to use
Sans Serif

Requirements
Must have
• All info; we would also like to make cards for individual staff members
• colors from our website and color palatte, attatched
• use same font and design as website for branding
Nice to have
• clean, simple card that has a pop of color
• we would like to see a few designs with our tag line "where smiles get brighter"
• we are not sure if we want to have it on there or not
• we would like to see a few designs incorporating the ribbon graphic on our website where the word WELCOME is

```html
<!DOCTYPE html>
<html lang="en">
<head>
<meta charset="utf-8">
<title>Maplebrook Pediatric Dentistry – Business Card</title>
<link rel="stylesheet" href="https://fonts.googleapis.com/css2?family=Source+Sans+3:wght@400;600;700&display=swap">
<style>
  :root {
    --backdrop: #824141;
    --card-front: #f3f3f3;
    --card-back: #222222;
    --sun-yellow: #f6b822;
    --berry: #c7288f;
    --ink: #1c1c1c;
    --rule: #b9b9b9;
    --white: #ffffff;
  }
  * { box-sizing: border-box; margin: 0; padding: 0; }
  html, body { width: 1200px; height: 900px; overflow: hidden; }
  body {
    position: relative;
    background: var(--backdrop);
    font-family: "Source Sans 3", "Helvetica Neue", Arial, sans-serif;
    color: var(--ink);
  }
  .card {
    position: absolute;
    top: 184px;
    width: 302px;
    height: 491px;
    border-radius: 14px;
  }
  .card--front { left: 299px; background: var(--card-front); text-align: center; }
  .card--back { left: 647px; background: var(--card-back); }

  .brand-dot {
    position: absolute;
    left: 50%;
    top: 38px;
    width: 46px;
    height: 46px;
    margin-left: -23px;
    border-radius: 50%;
    background: var(--sun-yellow);
  }
  .brand-name {
    position: absolute;
    left: 0; right: 0;
    top: 98px;
    font-size: 27px;
    font-weight: 600;
    line-height: 1.15;
    color: var(--sun-yellow);
  }

  .doctors { position: absolute; left: 0; right: 0; top: 231px; }
  .doctor-name { font-size: 19px; font-weight: 600; line-height: 21px; }
  .doctor-name .credential { color: var(--sun-yellow); font-weight: 400; }
  .doctor-email { font-size: 13.5px; line-height: 19px; margin-bottom: 1px; }

  .rule {
    position: absolute;
    left: 86px;
    width: 141px;
    height: 1px;
    background: var(--rule);
  }
  .rule--upper { top: 333px; }
  .rule--lower { top: 396px; }

  .contact { position: absolute; left: 0; right: 0; top: 348px; font-size: 13.5px; line-height: 19px; }
  .contact .label { color: var(--berry); }

  .address { position: absolute; left: 0; right: 0; top: 405px; font-size: 13.5px; line-height: 19px; font-style: normal; }

  .back-name {
    position: absolute;
    left: 48px;
    top: 366px;
    color: var(--white);
    font-size: 25px;
    font-weight: 600;
    line-height: 1.1;
  }
</style>
</head>
<body>
  <section class="card card--front" aria-label="Business card front">
    <span class="brand-dot" aria-hidden="true"></span>
    <p class="brand-name">Maplebrook<br>Pediatric Dentistry</p>

    <div class="doctors">
      <p class="doctor-name">Colette Varnum, <span class="credential">DMD</span></p>
      <p class="doctor-email">Colette@maplebrookkidsdental.example</p>
      <p class="doctor-name">Mara Tevlin, <span class="credential">DMD</span></p>
      <p class="doctor-email">Mara@maplebrookkidsdental.example</p>
    </div>

    <span class="rule rule--upper"></span>
    <div class="contact">
      <p><span class="label">P</span>: 555.419.3067</p>
      <p><span class="label">W</span>: www.maplebrookkidsdental.example</p>
    </div>
    <span class="rule rule--lower"></span>

    <address class="address">
      <p>Maplebrook Pediatric Dentistry</p>
      <p>482 Orchard Vale Road Suite 517</p>
      <p>Fernhollow, PA 17000</p>
    </address>
  </section>

  <section class="card card--back" aria-label="Business card back">
    <p class="back-name">Maplebrook<br>Pediatric Dentistry</p>
  </section>
</body>
</html>
```